Meadowtail Pet Business Card

We need a business card designed with two sides to it. I would like the front of the card to be mostly graphic and the back of the card to have the bullet points of our pet food.

I don't have a telephone number for the business yet so just leave a space for a toll free number. (800) xxx-xxxx.

Thanks,

Tobias

Combination Diet
Chicken Diet
Beef Diet
Lamb Diet

Website:  www.meadowtailpet-example.net

email:  rwelby@meadowtailpet-example.net

Direct - 347-xxx-xxxx
Toll Free - xxx-xxx-xxxx

www.meadowtailpet-example.net

Ravi Welby (Example)
Customer Experience Officer

rwelby@meadowtailpet-example.net
Direct - (347) xxx-xxxx

Sales Inquiries - (800) xxx-xxxx

All,

Please include the following items on the back of the business card.

Combination Diet
Chicken Diet
Beef Diet
Lamb Diet
 

Thanks,

Tobias

All, I will also want a QR code on the front or back of the card that can be scanned by a smart phone with our individual contact information.  Thanks, Tobias

Industry/Entity Type

Pet

```html
<!DOCTYPE html>
<html lang="en">
<head>
<meta charset="utf-8">
<title>Meadowtail Pet Business Card</title>
<link rel="stylesheet" href="https://fonts.googleapis.com/css2?family=Caladea:ital,wght@1,400;1,700&display=swap">
<style>
  :root {
    --table: #efe9e1;
    --rust: #b8432a;
    --ember: #d86a26;
    --sun-core: #ffe800;
    --sun-edge: #f6b000;
    --ink: #1c130a;
    --silhouette: #2a170c;
    --silhouette-soft: #5a2a12;
  }
  * { box-sizing: border-box; margin: 0; padding: 0; }
  html, body { width: 1200px; height: 1200px; overflow: hidden; }
  body {
    background: var(--table);
    font-family: "Caladea", "Cambria", Georgia, serif;
    font-style: italic;
    color: var(--ink);
    display: flex;
    flex-direction: column;
    align-items: center;
    justify-content: center;
    gap: 40px;
  }
  .card {
    position: relative;
    width: 980px;
    height: 560px;
    overflow: hidden;
    box-shadow: 0 6px 18px rgba(0,0,0,.18);
  }
  .card-art { position: absolute; inset: 0; width: 100%; height: 100%; }
  .card-text { position: absolute; line-height: 1.15; white-space: nowrap; }

  /* back side */
  .diet-list {
    top: 70px; left: 430px;
    list-style: none;
    font-size: 36px;
  }
  .diet-list li::before { content: "\2022"; margin-right: 8px; }
  .diet-list li:nth-child(2) { padding-left: 8px; }
  .diet-list li:nth-child(3) { padding-left: 4px; }
  .web-contact { left: 50px; bottom: 70px; font-size: 28px; }
  .phone-contact { right: 40px; bottom: 40px; font-size: 30px; text-align: right; }

  /* front side */
  .brand {
    top: 40px; left: 44px;
    display: flex; align-items: center; gap: 14px;
    font-size: 40px; font-weight: 700;
  }
  .brand-mark { width: 34px; height: 34px; background: var(--ink); }
  .holder { top: 230px; left: 0; width: 680px; text-align: center; }
  .holder-name { font-size: 52px; font-weight: 700; }
  .holder-title { font-size: 34px; }
  .direct-contact { right: 190px; bottom: 50px; font-size: 34px; text-align: right; }
</style>
</head>
<body>

  <section class="card card-back" aria-label="Business card back">
    <svg class="card-art" viewBox="0 0 980 560">
      <defs>
        <radialGradient id="back-sun" cx="0.5" cy="0.5" r="0.5">
          <stop offset="0.55" stop-color="var(--sun-core)"/>
          <stop offset="1" stop-color="var(--sun-edge)"/>
        </radialGradient>
        <linearGradient id="back-sky" x1="0" y1="0" x2="1" y2="0">
          <stop offset="0" stop-color="var(--rust)"/>
          <stop offset="1" stop-color="var(--ember)"/>
        </linearGradient>
        <linearGradient id="back-tree" x1="0" y1="0" x2="0" y2="1">
          <stop offset="0" stop-color="var(--silhouette)"/>
          <stop offset="1" stop-color="var(--silhouette-soft)"/>
        </linearGradient>
      </defs>
      <rect width="980" height="560" fill="url(#back-sky)"/>
      <circle cx="560" cy="330" r="360" fill="url(#back-sun)"/>
      <rect role="img" aria-label="Acacia tree silhouette at sunset" x="780" y="60" width="200" height="300" rx="24" fill="url(#back-tree)"/>
    </svg>
    <ul class="card-text diet-list">
      <li>Combination Diet</li>
      <li>Chicken Diet</li>
      <li>Beef Diet</li>
      <li>Lamb Diet</li>
    </ul>
    <div class="card-text web-contact">
      <p>Website:&nbsp; www.meadowtailpet-example.net</p>
      <p>email:&nbsp; rwelby@meadowtailpet-example.net</p>
    </div>
    <div class="card-text phone-contact">
      <p>Direct - 347-xxx-xxxx</p>
      <p>Toll Free - xxx-xxx-xxxx</p>
    </div>
  </section>

  <section class="card card-front" aria-label="Business card front">
    <svg class="card-art" viewBox="0 0 980 560">
      <defs>
        <radialGradient id="front-sun" cx="0.5" cy="0.5" r="0.5">
          <stop offset="0.55" stop-color="var(--sun-core)"/>
          <stop offset="1" stop-color="var(--sun-edge)"/>
        </radialGradient>
        <linearGradient id="front-sky" x1="0" y1="0" x2="1" y2="0">
          <stop offset="0" stop-color="var(--rust)"/>
          <stop offset="1" stop-color="var(--ember)"/>
        </linearGradient>
        <linearGradient id="front-tree" x1="0" y1="0" x2="0" y2="1">
          <stop offset="0" stop-color="var(--silhouette)"/>
          <stop offset="1" stop-color="var(--silhouette-soft)"/>
        </linearGradient>
      </defs>
      <rect width="980" height="560" fill="url(#front-sky)"/>
      <circle cx="420" cy="400" r="420" fill="url(#front-sun)"/>
      <rect role="img" aria-label="Acacia tree silhouette at sunset" x="720" y="20" width="260" height="380" rx="28" fill="url(#front-tree)"/>
    </svg>
    <div class="card-text brand">
      <span class="brand-mark" aria-hidden="true"></span>
      <span class="brand-name">meadowtailpet</span>
    </div>
    <div class="card-text holder">
      <p class="holder-name">Ravi Welby</p>
      <p class="holder-title">Customer Experience Officer</p>
    </div>
    <div class="card-text direct-contact">
      <p>rwelby@meadowtailpet-example.net</p>
      <p>Direct - (347) xxx-xxxx</p>
    </div>
  </section>

</body>
</html>
```